landscaping core flute signs

I need core flutes created with business name and a few extra dot points for putting on fences for job sites 120cm x 120cm approx.
I want our old ones information with the new L logo and colour palette

```html
<!DOCTYPE html>
<html lang="en">
<head>
<meta charset="utf-8">
<title>Stoneleaf Works – Site Signs</title>
<link href="https://fonts.googleapis.com/css2?family=Cinzel:wght@500&family=Oswald:wght@300;400;600&display=swap" rel="stylesheet">
<style>
  :root {
    --green: #5f8d58;
    --black: #000000;
    --white: #ffffff;
    --backdrop: #b3b3b3;
    --soft-grey: #c9c9c9;
  }
  * { box-sizing: border-box; margin: 0; padding: 0; }
  html, body { width: 1200px; height: 631px; overflow: hidden; }
  body { background: var(--backdrop); position: relative; font-family: "Oswald", sans-serif; }

  .sign {
    position: absolute; top: 53px; width: 514px; height: 525px;
    background: var(--white); color: var(--black);
    box-shadow: 0 18px 22px -14px rgba(0,0,0,.35);
    --box-bg: var(--black); --box-text: var(--white); --bar-bg: var(--black); --bar-text: var(--white);
  }
  .sign--light { left: 58px; }
  .sign--dark {
    left: 620px; background: var(--black); color: var(--white);
    --box-bg: var(--white); --box-text: var(--black); --bar-bg: var(--white); --bar-text: var(--black);
  }

  .brand-dot {
    position: absolute; left: 179px; top: 23px; width: 156px; height: 156px;
    border-radius: 50%; background: var(--green);
  }
  .brand-name {
    position: absolute; left: 0; right: 0; top: 194px; text-align: center;
    font-family: "Cinzel", serif; font-weight: 500; font-size: 46px; line-height: 50px; letter-spacing: 1px;
  }
  .brand-sub {
    position: absolute; left: 0; right: 0; top: 250px; display: flex; align-items: center; justify-content: center; gap: 14px;
    font-family: "Cinzel", serif; font-weight: 500; font-size: 27px; line-height: 30px; letter-spacing: 12px;
  }
  .brand-sub .rule { width: 74px; height: 2px; background: currentColor; }
  .brand-sub .word { margin-right: -12px; }
  .tagline {
    position: absolute; left: 0; right: 0; top: 281px; text-align: center; padding-left: 5px;
    font-family: "Cinzel", serif; font-size: 12px; line-height: 14px; letter-spacing: 5px; color: var(--green);
  }

  .service {
    position: absolute; top: 331px; width: 147px; height: 114px;
    background: var(--box-bg); color: var(--box-text); border-radius: 20px;
    text-align: center;
  }
  .service::after {
    content: ""; position: absolute; inset: 6px 5px 5px 6px; border-radius: 16px;
    border-right: 2px solid var(--soft-grey); border-bottom: 2px solid var(--soft-grey);
    opacity: .7;
  }
  .service--paving { left: 26px; }
  .service--fencing { left: 183px; }
  .service--design { left: 342px; }
  .service-icon {
    position: absolute; left: 37px; top: -31px; width: 73px; height: 73px; border-radius: 50%;
    background: var(--green); border: 6px solid var(--white);
    display: flex; align-items: center; justify-content: center;
  }
  .sign--dark .service-icon { border-color: var(--black); }
  .service-label {
    position: absolute; left: 0; right: 0; top: 48px;
    font-weight: 600; font-size: 25px; line-height: 23px; text-transform: uppercase; letter-spacing: -.3px;
  }

  .contact-bar { position: absolute; left: 0; top: 471px; width: 514px; height: 54px; }
  .contact-band { position: absolute; left: 0; top: 0; }
  .phone {
    position: absolute; left: 31px; top: 0; height: 54px; display: flex; align-items: center; gap: 9px;
    color: var(--white); font-weight: 400; font-size: 36px; line-height: 1; letter-spacing: .5px;
  }
  .phone-icon, .email-icon { flex: none; display: block; }
  .email {
    position: absolute; left: 297px; top: 17px; height: 37px; display: flex; align-items: center; gap: 9px;
    color: var(--bar-text); font-weight: 300; font-size: 18px; line-height: 1;
  }
</style>
</head>
<body>

<section class="sign sign--light">
  <div class="brand-dot"></div>
  <h1 class="brand-name">STONELEAF</h1>
  <div class="brand-sub"><span class="rule"></span><span class="word">WORKS</span><span class="rule"></span></div>
  <p class="tagline">STRUCTURAL LANDSCAPING</p>

  <div class="service service--paving">
    <div class="service-icon">
      <svg width="38" height="30" viewBox="0 0 38 30" fill="none" stroke="#fff" stroke-width="2"><rect x="2" y="6" width="20" height="14" rx="5"/><path d="M22 10h7l6 7v6H2"/><circle cx="9" cy="24" r="3.5" fill="#5f8d58"/><circle cx="28" cy="24" r="3.5" fill="#5f8d58"/></svg>
    </div>
    <p class="service-label">Paving &amp;<br>Concreting</p>
  </div>
  <div class="service service--fencing">
    <div class="service-icon">
      <svg width="36" height="30" viewBox="0 0 36 30" fill="none" stroke="#fff" stroke-width="2"><path d="M3 28V6l3-3 3 3v22M14 28V6l3-3 3 3v22M25 28V6l4-3 4 3v22M9 10h5M9 22h5M20 10h5M20 22h5"/></svg>
    </div>
    <p class="service-label">Fencing &amp;<br>Retaining</p>
  </div>
  <div class="service service--design">
    <div class="service-icon">
      <svg width="34" height="34" viewBox="0 0 34 34" fill="none" stroke="#fff" stroke-width="2"><path d="M5 15a12 12 0 0 1 24 0M3 15h28M14 4v6M20 4v6"/><circle cx="17" cy="25" r="6"/><circle cx="17" cy="25" r="2"/></svg>
    </div>
    <p class="service-label">Design &amp;<br>Construct</p>
  </div>

  <div class="contact-bar">
    <svg class="contact-band" width="514" height="54" viewBox="0 0 514 54"><polygon points="0,0 262,0 294,54 0,54" fill="var(--green)"/><polygon points="272,17 514,17 514,54 304,54" fill="var(--bar-bg)"/></svg>
    <div class="phone">
      <svg class="phone-icon" width="27" height="27" viewBox="0 0 27 27"><rect width="27" height="27" rx="6" fill="#fff"/><path d="M8 6l3 4-2 2a10 10 0 0 0 6 6l2-2 4 3-2 3C12 22 5 15 5 8z" fill="none" stroke="#5f8d58" stroke-width="1.8"/></svg>
      <span>0400 123 456</span>
    </div>
    <div class="email">
      <svg class="email-icon" width="22" height="17" viewBox="0 0 22 17"><rect x="1" y="1" width="20" height="15" rx="3" fill="var(--bar-text)"/><path d="M4 5l7 5 7-5" fill="none" stroke="var(--bar-bg)" stroke-width="1.8"/></svg>
      <span>sam@stoneleafworks.com</span>
    </div>
  </div>
</section>

<section class="sign sign--dark">
  <div class="brand-dot"></div>
  <h1 class="brand-name">STONELEAF</h1>
  <div class="brand-sub"><span class="rule"></span><span class="word">WORKS</span><span class="rule"></span></div>
  <p class="tagline">STRUCTURAL LANDSCAPING</p>

  <div class="service service--paving">
    <div class="service-icon">
      <svg width="38" height="30" viewBox="0 0 38 30" fill="none" stroke="#fff" stroke-width="2"><rect x="2" y="6" width="20" height="14" rx="5"/><path d="M22 10h7l6 7v6H2"/><circle cx="9" cy="24" r="3.5" fill="#5f8d58"/><circle cx="28" cy="24" r="3.5" fill="#5f8d58"/></svg>
    </div>
    <p class="service-label">Paving &amp;<br>Concreting</p>
  </div>
  <div class="service service--fencing">
    <div class="service-icon">
      <svg width="36" height="30" viewBox="0 0 36 30" fill="none" stroke="#fff" stroke-width="2"><path d="M3 28V6l3-3 3 3v22M14 28V6l3-3 3 3v22M25 28V6l4-3 4 3v22M9 10h5M9 22h5M20 10h5M20 22h5"/></svg>
    </div>
    <p class="service-label">Fencing &amp;<br>Retaining</p>
  </div>
  <div class="service service--design">
    <div class="service-icon">
      <svg width="34" height="34" viewBox="0 0 34 34" fill="none" stroke="#fff" stroke-width="2"><path d="M5 15a12 12 0 0 1 24 0M3 15h28M14 4v6M20 4v6"/><circle cx="17" cy="25" r="6"/><circle cx="17" cy="25" r="2"/></svg>
    </div>
    <p class="service-label">Design &amp;<br>Construct</p>
  </div>

  <div class="contact-bar">
    <svg class="contact-band" width="514" height="54" viewBox="0 0 514 54"><polygon points="0,0 262,0 294,54 0,54" fill="var(--green)"/><polygon points="272,17 514,17 514,54 304,54" fill="var(--bar-bg)"/></svg>
    <div class="phone">
      <svg class="phone-icon" width="27" height="27" viewBox="0 0 27 27"><rect width="27" height="27" rx="6" fill="#fff"/><path d="M8 6l3 4-2 2a10 10 0 0 0 6 6l2-2 4 3-2 3C12 22 5 15 5 8z" fill="none" stroke="#5f8d58" stroke-width="1.8"/></svg>
      <span>0400 123 456</span>
    </div>
    <div class="email">
      <svg class="email-icon" width="22" height="17" viewBox="0 0 22 17"><rect x="1" y="1" width="20" height="15" rx="3" fill="var(--bar-text)"/><path d="M4 5l7 5 7-5" fill="none" stroke="var(--bar-bg)" stroke-width="1.8"/></svg>
      <span>sam@stoneleafworks.com</span>
    </div>
  </div>
</section>

</body>
</html>
```